Business Card Design Project for Web Development Company

Need a professional card that stands out with both color and texture.
We provide websites and web development services for small businesses with a focus on connections. Examples include: Automotive repair shop, we take their repair logs and make them available online so their customers can view, print and share (when selling) their maintenance records. Vet clinic, we create systems where customers can sign up for a recurring payment program for the annual wellness checks on their pets and get reminders when it's time, then see and schedule their own appointments. Etc... So not simply a website, but one that connects systems or customers to the business.
Important - !!!!We will be using http://inkvaleprinters.com/ for the cards, so take a look at what options are available for business card printing, they can do a lot of cool things!!!!
You can pick any 1-3 options from inkvaleprinters. I'm leaning towards a black background, but the logo will work on any color.
Front:
Marcus Telford
2750 SW 8th Ave STE 214-587
Larkmont, WA 98412
555-617-2038 - cell
555-259-7306 - office
marcus@sitelinkhub.com
www.SiteLinkHub.com
Updates
We provide websites and web development services for small businesses with a focus on connections. Examples include: Automotive repair shop, we take their repair logs and make them available online so their customers can view, print and share (when selling) their maintenance records. Vet clinic, we create systems where customers can sign up for a recurring payment program for the annual wellness checks on their pets and get reminders when it''s time, then see and schedule their own appointments. Etc... So not simply a website, but one that connects systems or customers to the business.
Target Market(s)
Small business owners
Industry/Entity Type
Automotive
Look and feel
Each slider illustrates characteristics of the customer's brand and the style your logo design should communicate.

```html
<!DOCTYPE html>
<html lang="en">
<head>
<meta charset="utf-8">
<title>SiteLinkHub Business Card</title>
<link rel="stylesheet" href="https://fonts.googleapis.com/css2?family=Open+Sans:wght@400;600;700&display=swap">
<style>
  :root {
    --page-bg: #d8d3ce;
    --card-back: #070708;
    --card-front: #2a2a2c;
    --card-band: #1b1b1c;
    --brand-blue: #2a8fd4;
    --text-light: #f2f2f2;
    --text-muted: #5a5d60;
    --icon-red: #c4262e;
  }
  * { box-sizing: border-box; margin: 0; padding: 0; }
  html, body { width: 1200px; height: 867px; overflow: hidden; }
  body {
    background: var(--page-bg);
    font-family: "Open Sans", Arial, sans-serif;
    position: relative;
  }
  .card {
    position: absolute;
    top: 273px;
    width: 560px;
    height: 320px;
    border-radius: 14px;
    overflow: hidden;
    box-shadow: 0 14px 30px rgba(0,0,0,0.35);
  }
  .card--back { left: 30px; background: var(--card-back); display: flex; align-items: center; justify-content: center; }
  .card--front { left: 610px; background: var(--card-front); }

  .brand {
    display: flex;
    align-items: center;
    gap: 10px;
    color: var(--brand-blue);
    font-weight: 700;
    letter-spacing: 0.5px;
  }
  .brand__dot { border-radius: 50%; background: var(--brand-blue); display: block; }
  .card--back .brand { font-size: 52px; }
  .card--back .brand__dot { width: 22px; height: 22px; }
  .card--front .brand { position: absolute; left: 32px; top: 30px; font-size: 30px; }
  .card--front .brand__dot { width: 13px; height: 13px; }

  .holder {
    position: absolute;
    left: 52px;
    top: 110px;
    font-size: 22px;
    line-height: 30px;
    color: var(--brand-blue);
    font-weight: 400;
  }
  .holder-line {
    position: absolute;
    left: 250px;
    top: 118px;
    width: 310px;
    height: 14px;
  }

  .contact {
    position: absolute;
    left: 52px;
    top: 172px;
    list-style: none;
    color: var(--text-light);
    font-size: 13.5px;
    font-weight: 600;
    line-height: 20px;
  }
  .contact li { display: flex; align-items: center; gap: 10px; }
  .contact svg { width: 11px; height: 11px; fill: var(--icon-red); flex: none; }

  .address {
    position: absolute;
    right: 40px;
    top: 168px;
    text-align: right;
    color: var(--brand-blue);
    font-size: 14px;
    font-weight: 600;
    line-height: 20px;
    font-style: normal;
  }

  .web-band {
    position: absolute;
    left: 0; right: 0; bottom: 0;
    height: 44px;
    background: var(--card-band);
    display: flex;
    align-items: center;
    justify-content: center;
    color: var(--text-muted);
    font-size: 20px;
    font-weight: 600;
  }
</style>
</head>
<body>
  <section class="card card--back" aria-label="Card back">
    <div class="brand"><span class="brand__dot"></span>SiteLinkHub</div>
  </section>

  <section class="card card--front" aria-label="Card front">
    <div class="brand"><span class="brand__dot"></span>SiteLinkHub</div>

    <h1 class="holder">Marcus Telford</h1>
    <svg class="holder-line" viewBox="0 0 310 14" aria-hidden="true">
      <line x1="5" y1="8" x2="302" y2="5" stroke="var(--brand-blue)" stroke-width="2.5"/>
      <circle cx="5" cy="8" r="4.5" fill="var(--brand-blue)"/>
      <circle cx="302" cy="5" r="6" fill="var(--brand-blue)"/>
    </svg>

    <ul class="contact">
      <li>
        <svg viewBox="0 0 12 12" aria-hidden="true"><path d="M3 0h6a1 1 0 0 1 1 1v10a1 1 0 0 1-1 1H3a1 1 0 0 1-1-1V1a1 1 0 0 1 1-1zm0 2v7h6V2z"/></svg>
        555-617-2038 - cell
      </li>
      <li>
        <svg viewBox="0 0 12 12" aria-hidden="true"><path d="M2.4 0.5 4.3 3 3.3 4.4a7 7 0 0 0 4.3 4.3L9 7.7l2.5 1.9-1 1.9C5 11.5 0.5 7 0.5 1.5z"/></svg>
        555-259-7306 - office
      </li>
      <li>
        <svg viewBox="0 0 12 12" aria-hidden="true"><path d="M0 2h12v8H0zm1 1 5 3.5L11 3z"/></svg>
        marcus@sitelinkhub.com
      </li>
    </ul>

    <address class="address">
      2750 SW 8th Ave STE 214-587<br>
      Larkmont, WA 98412
    </address>

    <div class="web-band">www.SiteLinkHub.com</div>
  </section>
</body>
</html>
```